Specialized tax accounting firm needs letterhead design

We need a letterhead design for a professional services firm called R. Desmond Pell Inc. The firm is essentially a very specialized tax accounting firm - instead of serving the end consumer, we support other public accounting firms in the area of Canadian and U.S. tax advisory and compliance (i.e. they call us on tax issues too complex for the general practitioner. Our byline is "Tax Support Services for Public Accounting Firms". Our letterhead should utilize our logo and be based on colours present in our logo (see file attached). The final design needs to convey professionalism and trustworthiness (we're hired by accountants after all!) while being creative and eye-catching.

I've attached:
The font used in the logo
The logo itself in a variety of file formats
A single page showing the key firm information which should be appearing in the letterhead

Please note that there is much more leather background around the logo than needs to be incorporated in the letterhead.

Industry/Entity Type

Accounting

```html
<!DOCTYPE html>
<html lang="en">
<head>
<meta charset="utf-8">
<title>R. Desmond Pell Inc. – Letterhead</title>
<link rel="stylesheet" href="https://fonts.googleapis.com/css2?family=Play:wght@400;700&display=swap">
<style>
  :root {
    --backdrop: #e4e4e4;
    --paper: #ececee;
    --band-dark: #0e0e0e;
    --band-mid: #2c2c2c;
    --ink: #111111;
    --band-text: #f2f2f2;
    --signature-ink: #8a9cc4;
  }
  * { margin: 0; padding: 0; box-sizing: border-box; }
  html, body {
    width: 1200px; height: 849px; overflow: hidden;
    background: var(--backdrop);
  }
  .letterhead {
    position: absolute;
    left: 298px; top: 125px;
    width: 480px; height: 676px;
    background: var(--paper);
    box-shadow: 0 4px 16px rgba(0,0,0,0.18);
    font-family: "Play", sans-serif;
    color: var(--ink);
  }
  .header-band {
    position: absolute; left: 0; top: 0; width: 100%; height: 88px;
    overflow: hidden;
  }
  .band-texture {
    position: absolute; inset: 0;
    background: radial-gradient(ellipse at 50% 40%, var(--band-mid) 0%, var(--band-dark) 75%);
  }
  .firm-identity {
    position: absolute; left: 0; right: 0; top: 22px;
    text-align: center; color: var(--band-text);
  }
  .firm-name {
    font-size: 22px; font-weight: 400; letter-spacing: 1px; line-height: 26px;
    white-space: nowrap;
  }
  .firm-byline {
    font-size: 7.5px; letter-spacing: 0.8px; margin-top: 6px;
    text-transform: uppercase; white-space: nowrap;
  }
  .salutation {
    position: absolute; left: 62px; top: 180px;
    font-size: 14px; font-weight: 700;
  }
  .letter-body {
    position: absolute; left: 62px; width: 356px; top: 223px;
  }
  .letter-body p {
    font-size: 7.9px; font-weight: 700; line-height: 13px;
    text-align: justify; margin-bottom: 12px;
  }
  .signature {
    position: absolute; left: 347px; top: 500px; width: 72px; height: 27px;
    background: linear-gradient(90deg, transparent, rgba(138,156,196,0.35), transparent);
    border-radius: 13px;
  }
  .footer-band {
    position: absolute; left: 0; bottom: 0; width: 100%; height: 28px;
    background: var(--band-dark);
    color: var(--band-text);
    font-size: 6px; letter-spacing: 0.3px;
    text-align: center; padding-top: 5px; line-height: 9px;
  }
  .footer-band span { margin: 0 4px; }
</style>
</head>
<body>
  <article class="letterhead">
    <header class="header-band">
      <div class="band-texture" role="img" aria-label="Dark leather texture background"></div>
      <div class="firm-identity">
        <div class="firm-name">R. Desmond Pell Inc.</div>
        <div class="firm-byline">Tax Support Services for Public Accounting Firms</div>
      </div>
    </header>

    <h1 class="salutation">Dear Mr. Smith,</h1>

    <section class="letter-body">
      <p>Lorem ipsum dolor sit amet, consectetur adipiscing elit. Donec orci purus, luctus vitae dignissim eu, iaculis sed purus. Vivamus faucibus, ipsum nec aliquet viverra, leo mauris condimentum ligula, sit amet sagittis enim ligula quis arcu. Nam egestas tortor id nisi porttitor mattis. In tortor ante, ultricies in suscipit a, tempus non massa. Vivamus et auctor mi. Fusce vel massa nulla. Phasellus nec eros mauris, et scelerisque orci.</p>
      <p>Donec malesuada orci vitae nulla accumsan porta a id massa. Quisque accumsan iaculis magna sit amet fringilla. Maecenas consequat, magna eget tincidunt semper, odio nibh rutrum mi, id feugiat ante nisi eu risus. Vestibulum nunc orci, rhoncus a placerat in, ultricies in mi. Cras mattis varius eros, vel fringilla nisi suscipit eget. Quisque scelerisque sagittis nulla at porttitor.</p>
      <p>Sed id augue vitae urna euismod commodo aliquet a quam. Pellentesque arcu velit, cursus et malesuada ut, consequat et diam. Nullam erat sem, rhoncus id ullamcorper vitae, rhoncus et arcu. In ultricies ultricies nulla, ut rutrum nisi iaculis at. Donec eu magna a metus ornare faucibus. Fusce aliquet faucibus ultricies. Morbi semper, est id tincidunt gravida, sem arcu adipiscing lacus, ac bibendum nulla leo eu purus. Quisque nec diam sed risus consectetur a ccumsan quis quis nibh. Vestibulum id purus lorem.</p>
    </section>

    <div class="signature" role="img" aria-label="Handwritten signature of the sender"></div>

    <footer class="footer-band">
      <div>18-410 Harbourview Road, Halifax, Nova Scotia, Canada B3K 2R7</div>
      <div><span>Phone 902.555.0142</span><span>Fax 902.555.0187</span><span>info@pelltaxsupport.ca</span><span>www.pelltaxsupport.ca</span></div>
    </footer>
  </article>
</body>
</html>
```